need this exactly copied with ZERO LOSS highest quality. Need vector. NO GRANULATION...GETTING LABELS DONE NEED THIS EXACTLY COPIED BUT IN ITS HIGHEST FORM SO WHEN THEY MAKE MY LABEL IT IS HIGHEST POSSIBLE QUALITY. LABEL IS 7 X 1.5 INCHES.

```html
<!DOCTYPE html>
<html lang="en">
<head>
<meta charset="utf-8">
<title>Soothing Cream Label</title>
<link href="https://fonts.googleapis.com/css2?family=Poppins:wght@400;500;600;700&family=Jost:wght@300;400;500&display=swap" rel="stylesheet">
<style>
  :root {
    --navy: #181b4a;
    --ink: #161a45;
    --label: #e3f3f8;
    --white: #ffffff;
  }
  * { margin: 0; padding: 0; box-sizing: border-box; }
  html, body { width: 1200px; height: 1200px; overflow: hidden; background: var(--navy); }
  .label {
    position: absolute; left: 37px; top: 479px; width: 1126px; height: 241px;
    background: var(--label); color: var(--ink);
    font-family: "Poppins", sans-serif;
    box-shadow: 6px 7px 8px rgba(5, 6, 25, 0.55);
  }
  .abs { position: absolute; }

  /* Left panel */
  .usage { left: 105px; top: 28px; width: 230px; }
  .heading { font-weight: 700; font-size: 9.6px; letter-spacing: 0.14em; line-height: 1; }
  .usage-text { font-weight: 500; font-size: 9.2px; line-height: 12px; margin-top: 1px; }
  .external { font-weight: 600; font-size: 8.8px; margin-top: 6px; }
  .note { font-weight: 500; font-size: 6.6px; line-height: 9.3px; margin-top: 1px; }
  .ingredients-title { margin-top: 6px; }
  .ingredients {
    width: 224px; font-weight: 500; font-size: 6.1px; line-height: 8.35px;
    text-align: justify; margin-top: 4px;
  }

  /* Centre panel */
  .product { left: 449px; top: 31px; }
  .kind {
    font-family: "Jost", sans-serif; font-weight: 300; font-size: 13px;
    letter-spacing: 0.32em; line-height: 1;
  }
  .name {
    font-weight: 600; font-size: 20.5px; letter-spacing: 0.12em;
    line-height: 27.5px; margin-top: 6px;
  }
  .name sup { font-size: 5px; font-weight: 500; letter-spacing: 0; vertical-align: 13px; }
  .volume { left: 449px; top: 196px; font-weight: 600; font-size: 10px; }
  .brand-mark {
    left: 592px; top: 168px; width: 110px; text-align: center;
    font-weight: 600; font-size: 10px; letter-spacing: 0.12em;
  }

  /* Right panel */
  .claims {
    right: 105px; top: 29px; text-align: right;
    font-weight: 600; font-size: 11.6px; letter-spacing: 0.14em; line-height: 20.8px;
  }
  .follow {
    right: 105px; top: 97px; font-weight: 700; font-size: 8px; letter-spacing: 0.12em;
  }
  .origin { right: 105px; top: 111px; font-size: 5px; font-weight: 500; }
  .distributor {
    right: 105px; top: 122px; text-align: right;
    font-family: "Jost", sans-serif; font-weight: 400; font-size: 5.7px;
    letter-spacing: 0.12em; line-height: 9px;
  }
  .distributor strong { font-weight: 500; }
  .code-space { right: 105px; top: 152px; width: 141px; height: 10px; background: var(--white); }
  .listing { right: 105px; top: 206px; font-weight: 700; font-size: 5.5px; }
</style>
</head>
<body>
  <main class="label">
    <section class="abs usage">
      <h2 class="heading">HOW TO USE</h2>
      <p class="usage-text">Apply a small amount onto the skin’s desired<br>area 1-3 times per day.</p>
      <p class="external">For external use only.</p>
      <p class="note">May help the appearance of dry, red, flaky skin.<br>This product is not designed to treat or cure eczema.</p>
      <h2 class="heading ingredients-title">INGREDIENTS</h2>
      <p class="ingredients">Aloe Barbadensis (Aloe Vera) Leaf Juice Organic, Helianthus Annuus (Sunflower) Seed Oil Organic, Emulsifying Wax NF, Stearic Acid, Vegetable Glycerin, Caprylic/Capric Triglyceride (Fractionated Coconut Oil), Butyrospermum Parkii (Shea Nut Butter) Organic, Avena Sativa (Colloidal Oatmeal) Kernel Flour, Simmondsia Chinensis (Jojoba) Seed Oil Organic, Polyacrylamide, C13-14 Isoparaffin, Laureth-7, Phenoxyethanol, Ethylhexylglycerin, Chondrus Crispus (Irish Moss) Extract, Oenothera Biennis (Evening Primrose) Oil Organic, Tocopherol (Vitamin E), Sodium Hyaluronate (Hyaluronic Acid), Linoleic Acid, Schinziophyton Rautanenii (Mongongo) Kernal Oil Virgin Organic, Bisabolol *With US and imported materials.</p>
    </section>

    <section class="abs product">
      <p class="kind">SOOTHING CREAM</p>
      <h1 class="name">THE TIDE<br>SOOTHED MY SKIN<sup>TM</sup></h1>
    </section>
    <p class="abs volume">4 fl oz / 118 mL</p>
    <p class="abs brand-mark">SALTWATER REMEDY</p>

    <section class="abs claims">
      <p>FOR ECZEMA-PRONE SKIN</p>
      <p>NATURAL FROM THE SEA</p>
      <p>OCEANIC MINERALS</p>
    </section>
    <p class="abs follow">FOLLOW US @saltwaterremedyco</p>
    <p class="abs origin">Made in the USA*</p>
    <p class="abs distributor"><strong>DISTRIBUTED BY</strong><br>SALTWATER REMEDY CO LLC<br>CORAL BAY SHORES FL, 33900</p>
    <div class="abs code-space"></div>
    <p class="abs listing">NEW The Tide Soothed My Skin Cream 4 fl oz / 118 mL</p>
  </main>
</body>
</html>
```